RM Cargoline businesscard project

RM Cargoline Ltd is a freshly founded small (3 employees), young (average age is 30 years) company, living from the road transportation market without own tools.
We would like to have an impressive, new-line, cool busines card for a freshly founded forwarding company on an overcrowded market which raises attention and makes the potential partners eager to work with us.

Target Market(s)

The main profile of the company is logistic/forwarding on road.

Industry/Entity Type

Freight Forwarding

Contact Information for Business Card

Name: Berki Zsófia
Title: general manager
mobile nr: +36-70/482-5193
fax nr: +36-1/534-9061
e-mail: zsofia.berki@rmcargoline.example
info@rmcargoline.example
website address: http://www.rmcargoline.example
and if possible maybe some funny or helpful info on the back

Requirements
Must have
• contact details above
Nice to have
• some really nice and catching back-side (info, graphics, useful tool info... anything)
Should not have
• trucks, road, ship, airplane on it...

```html
<!DOCTYPE html>
<html lang="en">
<head>
<meta charset="utf-8">
<title>RM Kordavix – Business Card</title>
<link href="https://fonts.googleapis.com/css2?family=Open+Sans:wght@400;600&display=swap" rel="stylesheet">
<style>
  :root {
    --brand-blue: #4a74a8;
    --name-blue: #5180b8;
    --ink: #1e1e1e;
    --logo-ink: #2a2a2a;
    --card-light: #fbfbfb;
    --card-shade: #d6d6d6;
    --page-bg: #e4e4e4;
  }
  * { margin: 0; padding: 0; box-sizing: border-box; }
  html, body {
    width: 1189px;
    height: 1200px;
    overflow: hidden;
    background: var(--page-bg);
    font-family: "Open Sans", "Segoe UI", sans-serif;
  }
  .business-card {
    position: absolute;
    left: 44px;
    top: 286px;
    width: 1100px;
    height: 628px;
    overflow: hidden;
    background: radial-gradient(ellipse at 45% 55%, var(--card-light) 0%, #efefef 45%, var(--card-shade) 100%);
    box-shadow: 0 6px 18px rgba(0,0,0,0.25);
  }
  .card-frame {
    position: absolute;
    inset: 0;
    width: 1100px;
    height: 628px;
  }
  .card-frame .band { fill: var(--brand-blue); }
  .card-frame .divider { stroke: var(--ink); stroke-width: 2.5; }

  .brand {
    position: absolute;
    left: 60px;
    top: 120px;
    width: 420px;
    display: flex;
    flex-direction: column;
    align-items: center;
  }
  .brand-square {
    width: 170px;
    height: 170px;
    background: var(--brand-blue);
    margin-bottom: 58px;
  }
  .brand-name {
    font-weight: 600;
    font-size: 52px;
    line-height: 1;
    color: var(--logo-ink);
    white-space: nowrap;
  }

  .person {
    position: absolute;
    left: 526px;
    top: 78px;
  }
  .person-name {
    font-size: 74px;
    font-weight: 400;
    line-height: 1;
    color: var(--name-blue);
    letter-spacing: -0.5px;
    white-space: nowrap;
  }
  .person-title {
    font-size: 32px;
    line-height: 1;
    color: var(--ink);
    margin-top: 10px;
    margin-left: 3px;
  }

  .contacts {
    position: absolute;
    left: 543px;
    top: 334px;
    list-style: none;
  }
  .contacts li {
    display: flex;
    align-items: center;
    height: 44px;
    font-size: 27px;
    color: var(--ink);
    white-space: nowrap;
    letter-spacing: -0.2px;
  }
  .contacts .icon {
    width: 22px;
    height: 22px;
    margin-right: 15px;
    flex: none;
  }
</style>
</head>
<body>
  <section class="business-card" aria-label="RM Kordavix business card">
    <svg class="card-frame" viewBox="0 0 1100 628" aria-hidden="true">
      <polygon class="band" points="0,0 406,0 365,59 67,59 67,416 0,477"/>
      <polygon class="band" points="1100,232 1100,628 626,628 685,574 1039,574 1039,274"/>
      <line class="divider" x1="507" y1="68" x2="507" y2="553"/>
    </svg>

    <div class="brand">
      <div class="brand-square"></div>
      <div class="brand-name">RM Kordavix</div>
    </div>

    <div class="person">
      <h1 class="person-name">Berki Zsófia</h1>
      <p class="person-title">general manager</p>
    </div>

    <ul class="contacts">
      <li>
        <svg class="icon" viewBox="0 0 22 22" aria-label="mobile">
          <rect width="22" height="22" fill="#111"/>
          <path d="M7 4 L9.5 4 L10.5 8 L9 9.2 Q10.5 12.5 13 14 L14.2 12.5 L18 13.5 L18 16 Q17 18 14.5 17.5 Q7.5 15 5 7.5 Q4.8 5 7 4 Z" fill="#fff"/>
        </svg>
        +36-70/482-5193
      </li>
      <li>
        <svg class="icon" viewBox="0 0 22 22" aria-label="fax">
          <rect width="22" height="22" fill="#111"/>
          <rect x="6" y="3" width="10" height="5" fill="#fff"/>
          <rect x="3" y="9" width="16" height="7" fill="#fff"/>
          <rect x="6" y="14" width="10" height="5" fill="#fff" stroke="#111" stroke-width="1"/>
        </svg>
        +36-1/534-9061
      </li>
      <li>
        <svg class="icon" viewBox="0 0 22 22" aria-label="email">
          <rect width="22" height="22" fill="#111"/>
          <rect x="3.5" y="6" width="15" height="10" fill="#fff"/>
          <path d="M3.5 6 L11 12 L18.5 6 M3.5 16 L9 11 M18.5 16 L13 11" stroke="#111" stroke-width="1.2" fill="none"/>
        </svg>
        info@rmkordavix.example
      </li>
      <li>
        <svg class="icon" viewBox="0 0 22 22" aria-label="website">
          <rect width="22" height="22" fill="#111"/>
          <circle cx="11" cy="11" r="7" fill="#fff"/>
          <path d="M7 8 Q9 7 10 9 Q9 11 11 12 Q12 14 10 16 M13 6 Q15 8 14 10 Q16 11 17 13" stroke="#111" stroke-width="1.4" fill="none"/>
        </svg>
        http://www.rmkordavix.example
      </li>
      <li>
        <svg class="icon" viewBox="0 0 22 22" aria-label="email">
          <rect width="22" height="22" fill="#111"/>
          <rect x="3.5" y="6" width="15" height="10" fill="#fff"/>
          <path d="M3.5 6 L11 12 L18.5 6 M3.5 16 L9 11 M18.5 16 L13 11" stroke="#111" stroke-width="1.2" fill="none"/>
        </svg>
        zsofia.berki@rmkordavix.example
      </li>
    </ul>
  </section>
</body>
</html>
```